The Deskwell (A new and exciting small Business support solution) Business Cards

The Deskwell Business Card Design

About us:
The Deskwell is a small business support solution, assisting businesses with any marketing, office management and human resource skills.

Objective
To be a small business lifesaver, to relieve busy professionals from mundane operations so they can focus on their businesses future through complete, reliable, efficient and effective client support. To have people say WOW what did we do before The Deskwell.

Industry/Entity Type

Small Business

Colors
0355a3
33a6d7

Requirements
Must have
• Must be similar to the look and feel of my website http://www.thedeskwell-example.com.au/

Must have:

Blue colour is 0094FF

The Logo

A Small Business Support Solution
- Human Resources
- Office Administration
- Marketing

Maribel Torvik
0462 837 105
maribeltorvik@thedeskwell-example.com.au
www.thedeskwell-example.com

```html
<!DOCTYPE html>
<html lang="en">
<head>
<meta charset="utf-8">
<title>The Deskwell – Business Cards</title>
<link rel="stylesheet" href="https://fonts.googleapis.com/css2?family=Ubuntu:wght@400;500;700&display=swap">
<style>
  :root {
    --stage: #1f2124;
    --card-white: #ffffff;
    --card-tint: #e6eff8;
    --ink: #161616;
    --navy: #0355a3;
    --sky: #33a6d7;
    --dots: #555555;
  }
  * { box-sizing: border-box; margin: 0; padding: 0; }
  html, body {
    width: 1200px;
    height: 926px;
    overflow: hidden;
    background: var(--stage);
    font-family: "Ubuntu", sans-serif;
  }
  .stage {
    width: 1200px;
    height: 926px;
    display: flex;
    flex-direction: column;
    align-items: center;
    justify-content: center;
    gap: 40px;
  }
  .card {
    position: relative;
    width: 700px;
    height: 400px;
    overflow: hidden;
  }

  .brand { text-align: center; color: var(--ink); }
  .brand-name {
    font-weight: 400;
    letter-spacing: -0.5px;
    line-height: 1;
  }
  .brand-tagline {
    font-weight: 400;
    letter-spacing: 0.3px;
  }

  /* Back of card */
  .card--back { background: var(--card-tint); }
  .card--back .brand {
    position: absolute;
    left: 50%;
    top: 50%;
    transform: translate(-50%, -50%);
    white-space: nowrap;
  }
  .card--back .brand-name { font-size: 44px; }
  .card--back .brand-tagline { font-size: 14px; margin-top: 8px; }

  /* Front of card */
  .card--front { background: var(--card-white); }
  .card--front .brand {
    position: absolute;
    left: 140px;
    top: 44px;
    width: 420px;
  }
  .card--front .brand-name { font-size: 48px; }
  .card--front .brand-tagline { font-size: 14px; margin-top: 6px; }

  .divider {
    position: absolute;
    left: 170px;
    top: 140px;
    width: 360px;
    border-top: 3px dotted var(--dots);
  }
  .contact {
    position: absolute;
    left: 110px;
    top: 160px;
    width: 480px;
    text-align: center;
    color: var(--ink);
  }
  .contact-name {
    font-size: 30px;
    font-weight: 700;
    letter-spacing: 1px;
    text-transform: uppercase;
  }
  .contact-phone { font-size: 27px; margin-top: 8px; }
  .contact-web { font-size: 19px; margin-top: 6px; }
  .contact-email { font-size: 18px; color: var(--sky); margin-top: 4px; }

  .services {
    position: absolute;
    left: 36px;
    right: 36px;
    bottom: 38px;
    display: flex;
    justify-content: space-between;
    font-size: 17px;
    letter-spacing: 2px;
    text-transform: uppercase;
    color: var(--navy);
  }
</style>
</head>
<body>
<main class="stage">

  <section class="card card--back" aria-label="Business card, back">
    <div class="brand">
      <div class="brand-name">The Deskwell</div>
      <div class="brand-tagline">A Small Business Support Solution</div>
    </div>
  </section>

  <section class="card card--front" aria-label="Business card, front">
    <div class="brand">
      <div class="brand-name">The Deskwell</div>
      <div class="brand-tagline">A Small Business Support Solution</div>
    </div>
    <div class="divider"></div>
    <div class="contact">
      <div class="contact-name">Maribel Torvik</div>
      <div class="contact-phone">+0462 837 105</div>
      <div class="contact-web">www.thedeskwell-example.com.au</div>
      <div class="contact-email">maribeltorvik@thedeskwell-example.com.au</div>
    </div>
    <div class="services">
      <span>Human Resources</span><span>-</span>
      <span>Office Administration</span><span>-</span>
      <span>Marketing</span>
    </div>
  </section>

</main>
</body>
</html>
```